Business Cards Needed for Innovative Healthcare Marketing Company

We are a marketing company focused on healthcare. Our company is all about rebranding yourself renewing your image and generating results. The phoenix stands for "reborn" or "rising" which we provide new brands for our clients we take their old brands and renew it with creativity and innovation. I am looking for a business card with color dimension. I have attached an example of a card I think has the look and feel of what I am trying to accomplish. I like that the card example has black and grey font colors, I like the font placement and the small logo, I really like the use of the colors on the right those are the colors of my logo. My logo is phoenix so maybe incorporating flames similar to that design. I would like the back a solid color maybe red with an opaque version of the logo and website. As a marketing company I am always open to creative liberty!

Target Market(s)

Doctors and business professionals.

Industry/Entity Type

Marketing

Contact Information for Business Card

Velmora Health Care Marketing
Dana Prewitt- CEO
#(407)555-0172
email-dana@velmora.com
website- velmora.com

Font styles to use
Sans Serif

Colors
ec1f27
f37122
ffc214
fbed22
fbf289
f04a50

Requirements
Must have
• The logo and required information
Nice to have
• icons by the information
Should not have
• child like font

```html
<!DOCTYPE html>
<html lang="en">
<head>
<meta charset="utf-8">
<title>Velmora Health Care Marketing – Business Cards</title>
<link href="https://fonts.googleapis.com/css2?family=Lato:wght@300;400;700&display=swap" rel="stylesheet">
<style>
  :root {
    --canvas: #e9e6e1;
    --card-white: #ffffff;
    --brand-red: #ec1f27;
    --brand-red-soft: #f04a50;
    --brand-orange: #f37122;
    --brand-amber: #ef8a24;
    --ink: #1c1c1c;
    --ink-grey: #4a4a4a;
    --logo-red: #c9343a;
  }
  * { margin: 0; padding: 0; box-sizing: border-box; }
  html, body {
    width: 1200px; height: 900px; overflow: hidden;
    background: var(--canvas);
    font-family: "Lato", Arial, sans-serif;
  }
  .stage { position: relative; width: 1200px; height: 900px; }

  .card {
    position: absolute;
    width: 525px; height: 300px;
    top: 300px;
    border-radius: 3px;
    overflow: hidden;
    box-shadow: 0 10px 26px rgba(0,0,0,.18);
  }

  /* Front */
  .card-front { left: 50px; background: var(--card-white); }
  .flame-art {
    position: absolute; right: 0; top: 0;
    width: 215px; height: 220px;
    background: linear-gradient(160deg, var(--brand-orange) 0%, var(--brand-amber) 100%);
    border-radius: 0 0 0 70% / 0 0 0 45%;
  }
  .front-brand { position: absolute; left: 30px; top: 74px; }
  .brand-row { display: flex; align-items: center; gap: 10px; }
  .brand-dot {
    width: 28px; height: 28px; border-radius: 50%;
    background: var(--brand-orange);
  }
  .brand-name {
    font-weight: 300; font-size: 36px; letter-spacing: 2px;
    color: var(--logo-red); line-height: 1;
  }
  .card-front .brand-tagline {
    margin-top: 6px; margin-left: 38px;
    padding-top: 5px;
    border-top: 1px solid var(--logo-red);
    font-weight: 300; font-size: 11px; letter-spacing: 1.4px;
    color: var(--logo-red);
    white-space: nowrap;
  }
  .contact { position: absolute; left: 80px; top: 180px; }
  .contact-name { font-size: 17px; font-weight: 700; color: var(--ink); margin-bottom: 6px; }
  .contact-name .role { color: var(--brand-red); }
  .contact-line {
    display: flex; align-items: center; gap: 8px;
    font-size: 13px; color: var(--ink-grey); margin-top: 4px;
  }
  .contact-icon { width: 14px; height: 14px; flex: none; }

  /* Back */
  .card-back { left: 625px; background: var(--brand-red); }
  .back-flame {
    position: absolute; left: 0; right: 0; bottom: 0; height: 150px;
    background: linear-gradient(180deg, rgba(240,74,80,0) 0%, rgba(240,74,80,.55) 100%);
  }
  .back-brand {
    position: absolute; left: 0; right: 0; top: 90px;
    text-align: center; color: #fff;
  }
  .back-brand .brand-name { color: #fff; font-size: 48px; letter-spacing: 4px; }
  .back-brand .brand-tagline {
    color: #fff; border-top: 1px solid rgba(255,255,255,.8);
    display: inline-block; margin: 8px 0 0; padding: 5px 6px 0;
    font-weight: 300; font-size: 14px; letter-spacing: 1.5px;
  }
  .back-web {
    margin-top: 22px;
    font-size: 13px; letter-spacing: 1px; color: rgba(255,255,255,.85);
  }
</style>
</head>
<body>
<main class="stage">

  <section class="card card-front">
    <div class="flame-art" role="img" aria-label="Stylised orange phoenix flame illustration"></div>

    <div class="front-brand">
      <div class="brand-row">
        <span class="brand-dot"></span>
        <span class="brand-name">VELMORA</span>
      </div>
      <div class="brand-tagline">HEALTHCARE MARKETING</div>
    </div>

    <div class="contact">
      <p class="contact-name">Dana Prewitt<span class="role">-CEO</span></p>
      <p class="contact-line">
        <svg class="contact-icon" viewBox="0 0 14 14"><rect width="14" height="14" rx="2" fill="#ec1f27"/><path d="M4 3.5l1.5-.5 1 2-1 .8a5 5 0 0 0 2.7 2.7l.8-1 2 1-.5 1.5C8 10 4 6 4 3.5z" fill="#fff"/></svg>
        #(407)555-0172
      </p>
      <p class="contact-line">
        <svg class="contact-icon" viewBox="0 0 14 14"><rect width="14" height="14" rx="2" fill="#ec1f27"/><rect x="3" y="4" width="8" height="6" fill="none" stroke="#fff" stroke-width="1"/><path d="M3 4l4 3 4-3" fill="none" stroke="#fff" stroke-width="1"/></svg>
        dana@velmora.com
      </p>
      <p class="contact-line">
        <svg class="contact-icon" viewBox="0 0 14 14"><rect width="14" height="14" rx="2" fill="#ec1f27"/><rect x="3" y="3.5" width="8" height="6" fill="none" stroke="#fff" stroke-width="1"/><path d="M5.5 11h3" stroke="#fff" stroke-width="1"/></svg>
        velmora.com
      </p>
    </div>
  </section>

  <section class="card card-back">
    <div class="back-flame" role="img" aria-label="Faint phoenix flame decoration"></div>
    <div class="back-brand">
      <div class="brand-name">VELMORA</div>
      <div class="brand-tagline">HEALTHCARE MARKETING</div>
      <p class="back-web">www.velmora.com</p>
    </div>
  </section>

</main>
</body>
</html>
```